2 guided dives on the North of Bonaire

2 guided shore dives on the North of Bonaire including authentic local lunch and drinks.
We offer an adventure for experienced divers to discover the dive sites on the north of the island.
Showing you the beauty of the reefs and tasting authentic local cuisine like goat or iguana combined with a stunning view of the surroundings.

Target Market(s)

Divers / tourism

Industry/Entity Type

Tourism / Diving

Font styles to use
Sans Serif

Colors
0054AA
0677BA
7BADD7
CADEEF
E8F1F8
0094D4
00A9DD
6FCCEA
C7EBF8
E9F6FB
F0912C
F2A743
F7CA91
FBE8D2
FDF5EE
EE7325
F08F49
F5BC92
FAE3D3
FDF4ED

Requirements
Must have
• Some of the pictures I uploaded and the food picture / bottom like in the pictures
Nice to have
• inviting to join us on the guided dives
Should not have
• Any picture I didn't provide

```html
<!DOCTYPE html>
<html lang="en">
<head>
<meta charset="utf-8">
<title>Reefline Dive – Guided Dives Flyer</title>
<link rel="stylesheet" href="https://fonts.googleapis.com/css2?family=Baloo+2:wght@700;800&family=Montserrat:ital,wght@0,500;0,600;0,700;1,500&family=Oswald:wght@500;600&display=swap">
<style>
  :root{
    --navy:#1f2f6b;
    --deep:#0b1f4a;
    --ocean:#0054AA;
    --sky:#00A9DD;
    --sky-light:#6FCCEA;
    --sky-pale:#C7EBF8;
    --orange:#F0912C;
    --orange-dark:#EE7325;
    --white:#ffffff;
    --paper:#f4f6f8;
    --page:#d9dbde;
  }
  *{box-sizing:border-box;margin:0;padding:0}
  html,body{width:1200px;height:1117px;overflow:hidden;background:var(--page)}
  .flyer{position:absolute;left:220px;top:24px;width:760px;height:1070px;background:var(--paper);overflow:hidden;font-family:"Montserrat",sans-serif;box-shadow:0 6px 24px rgba(0,0,0,.18)}
  .backdrop{position:absolute;inset:0}
  .headline{position:absolute;left:58px;top:28px;font-family:"Baloo 2",sans-serif;font-weight:800;line-height:.9}
  .headline .lead{display:block;color:var(--white);font-size:46px;margin-left:14px}
  .headline .big{font-size:120px;color:var(--orange);letter-spacing:-1px}
  .headline .big em{font-style:normal;color:var(--sky-light)}
  .offer{position:absolute;left:58px;top:238px;width:630px;height:112px;border:4px solid var(--orange);border-radius:16px;display:flex;align-items:center;gap:18px;padding:0 24px}
  .offer .count{font-family:"Baloo 2",sans-serif;font-weight:800;font-size:104px;color:var(--sky-light);line-height:1}
  .offer .what{font-family:"Baloo 2",sans-serif;font-weight:700;font-size:34px;line-height:1.05;color:var(--white)}
  .perks{position:absolute;left:64px;top:374px;list-style:none;color:var(--white);font-size:22px;font-weight:600;width:640px}
  .perks li{display:flex;gap:14px;margin-bottom:14px;line-height:1.25}
  .perks svg{flex:none;margin-top:4px}
  .lunch{position:absolute;left:64px;top:470px;width:560px;color:var(--sky-light);font-style:italic;font-weight:500;font-size:22px;line-height:1.3}
  .photo{position:absolute;border-radius:50%;border:8px solid var(--navy);box-shadow:0 6px 14px rgba(0,0,0,.3)}
  .brand{position:absolute;left:36px;top:918px;display:flex;align-items:center;gap:10px;font-family:"Baloo 2",sans-serif;font-weight:800;font-size:30px;color:var(--navy)}
  .brand .dot{width:24px;height:24px;border-radius:50%;background:var(--orange)}
  .web{position:absolute;left:262px;top:912px;width:400px;height:62px;border:3px solid var(--orange);border-radius:31px;display:flex;align-items:center;gap:12px;padding-left:6px}
  .web .globe{width:48px;height:48px;border-radius:50%;background:var(--orange);display:flex;align-items:center;justify-content:center}
  .web small{display:block;font-size:12px;font-weight:600;color:var(--sky);letter-spacing:1px}
  .web b{display:block;font-size:24px;color:var(--navy);font-weight:700;line-height:1.05}
  .badge{position:absolute;left:684px;top:912px;width:58px;height:58px;border-radius:50%;background:var(--ocean)}
  .call{position:absolute;left:0;bottom:0;width:330px;height:92px;background:var(--orange);clip-path:polygon(0 0,92% 0,100% 100%,0 100%);color:var(--white);padding:14px 0 0 32px}
  .call small{display:block;font-size:15px;font-weight:700;letter-spacing:2px;margin-left:38px}
  .call .num{display:flex;align-items:center;gap:10px;font-family:"Oswald",sans-serif;font-weight:600;font-size:34px;line-height:1.1}
  .contact{position:absolute;right:0;bottom:0;width:460px;height:76px;background:var(--navy);clip-path:polygon(4% 0,100% 0,100% 100%,0 100%);color:var(--white);font-size:17px;padding:12px 0 0 46px}
  .contact p{display:flex;align-items:center;gap:8px;line-height:1.4}
  .strip{position:absolute;right:0;bottom:76px;width:460px;height:6px;background:var(--orange)}
</style>
</head>
<body>
<article class="flyer">
  <svg class="backdrop" width="760" height="1070" viewBox="0 0 760 1070">
    <defs>
      <radialGradient id="sea" cx="55%" cy="35%" r="75%">
        <stop offset="0" stop-color="#1f5a96"/>
        <stop offset=".6" stop-color="#123a72"/>
        <stop offset="1" stop-color="#0b1f4a"/>
      </radialGradient>
      <linearGradient id="foam" x1="0" y1="0" x2="1" y2="1">
        <stop offset="0" stop-color="#C7EBF8"/>
        <stop offset="1" stop-color="#E9F6FB" stop-opacity="0"/>
      </linearGradient>
    </defs>
    <path d="M0 590 Q70 590 110 640 Q140 690 110 730 L0 730 Z" fill="url(#foam)"/>
    <path role="img" aria-label="Underwater scene with a school of fish in deep blue water" fill="url(#sea)"
      d="M0 0 H760 V600 Q760 690 660 690 Q500 680 400 720 Q250 770 180 710 Q140 660 100 630 Q50 598 0 600 Z"/>
  </svg>

  <h1 class="headline"><span class="lead">Let us</span><span class="big">guide <em>you!</em></span></h1>

  <div class="offer">
    <span class="count">2</span>
    <span class="what">guided dives at<br>the North side of Bonaire</span>
  </div>

  <ul class="perks">
    <li><svg width="18" height="14" viewBox="0 0 18 14"><path d="M2 7 L7 12 L16 2" stroke="#F0912C" stroke-width="3.5" fill="none"/></svg>We show you the cool stuff</li>
    <li><svg width="18" height="14" viewBox="0 0 18 14"><path d="M2 7 L7 12 L16 2" stroke="#F0912C" stroke-width="3.5" fill="none"/></svg>You just enjoy the dives, we take care of the rest</li>
  </ul>
  <p class="lunch">Authentic local lunch and drinks at Posada Vista Mar</p>

  <div class="photo" role="img" aria-label="Seahorse on the reef" style="left:48px;top:694px;width:124px;height:124px;background:radial-gradient(circle,#3a8f9a,#164e66)"></div>
  <div class="photo" role="img" aria-label="Rocky northern coastline under blue sky" style="left:172px;top:710px;width:146px;height:146px;background:linear-gradient(#3d7fc4 45%,#8a8f8a 55%,#5d5a52)"></div>
  <div class="photo" role="img" aria-label="Plates of authentic local lunch" style="left:306px;top:716px;width:184px;height:184px;background:radial-gradient(circle,#d89a4a,#a35a2a 60%,#6b3b26)"></div>
  <div class="photo" role="img" aria-label="Turquoise bay seen from the shore" style="left:482px;top:710px;width:146px;height:146px;background:linear-gradient(#5aa7dd 40%,#1fa5c0 60%,#d9cdb1)"></div>
  <div class="photo" role="img" aria-label="Beach with palm shade and clear water" style="left:620px;top:694px;width:124px;height:124px;background:linear-gradient(#7ab8e4 40%,#34b5c8 60%,#e0d6bd)"></div>

  <div class="brand"><span class="dot"></span>Reefline Dive</div>

  <div class="web">
    <span class="globe"><svg width="26" height="26" viewBox="0 0 26 26" fill="none" stroke="#fff" stroke-width="2"><circle cx="13" cy="13" r="11"/><ellipse cx="13" cy="13" rx="5" ry="11"/><path d="M2 13h22M4 7h18M4 19h18"/></svg></span>
    <span><small>VISIT OUR WEBSITE</small><b>www.reefline-dive.com</b></span>
  </div>
  <div class="badge" role="img" aria-label="Dive certification badge"></div>

  <div class="strip"></div>
  <div class="call">
    <small>CALL US</small>
    <span class="num"><svg width="26" height="26" viewBox="0 0 26 26"><circle cx="13" cy="13" r="13" fill="#fff"/><path d="M9 7c1 0 2 2 2 3s-1 1-1 2 3 4 4 4 1-1 2-1 3 1 3 2-1 2-3 2c-4 0-9-5-9-9 0-2 1-3 2-3z" fill="#F0912C"/></svg>+(599) 700 12 34</span>
  </div>
  <div class="contact">
    <p><svg width="14" height="12" viewBox="0 0 14 12"><rect x="1" y="1" width="12" height="10" rx="2" fill="none" stroke="#6FCCEA" stroke-width="1.6"/><path d="M1 2l6 5 6-5" fill="none" stroke="#6FCCEA" stroke-width="1.6"/></svg>hello@reefline-dive.com</p>
    <p><svg width="12" height="16" viewBox="0 0 12 16"><path d="M6 15S1 9 1 6a5 5 0 0 1 10 0c0 3-5 9-5 9z" fill="#6FCCEA"/><circle cx="6" cy="6" r="2" fill="#1f2f6b"/></svg>kaya mariposa 12, Kralendijk, Bonaire</p>
  </div>
</article>
</body>
</html>
```